Update, redesign www.quorvane.net. Put it on WordPress and migrate to new host site

My current website is www.quorvane.net. The text content is ok but the site look and feel is several years old and does not project a sense of innovation. I am looking for a more modern exciting look. It needs to be built on word press and I need help in in putting it with a new hosting service.

Target Market(s)

Established organizations

Industry/Entity Type

Business Consultant

Number of Pages Required

1 page

Font styles to use
Sans Serif

Colors

Designer to choose colors to be used in the design.

Requirements
Must have
• Simple. Easy to read and navigate
Nice to have
• Innovation, creativity especially the leadership of innovation. Reading the current text on www.quorvane.net should help you with ideas
Should not have
• Difficulty in me managing or adding content after it is built

```html
<!DOCTYPE html>
<html lang="en">
<head>
<meta charset="utf-8">
<title>Quorvane — Innovation at Work</title>
<link href="https://fonts.googleapis.com/css2?family=Montserrat:wght@400;500;600;700&family=Open+Sans:wght@400;600;700&family=Arimo:wght@400;700&display=swap" rel="stylesheet">
<style>
:root{
  --red:#c8102e;
  --red-dark:#b0191e;
  --ink:#222;
  --text:#333;
  --muted:#555;
  --blue-icon:#3d7fd6;
  --band-a:#9ec4f0;
  --band-b:#6ea5e6;
  --card-line:#cfcfcf;
  --pale:#f5f5f5;
  --footer:#2c2c2c;
  --footer-bottom:#232323;
  --footer-text:#d8d8d8;
  --white:#fff;
}
*{box-sizing:border-box;margin:0;padding:0}
html,body{width:1200px;height:2628px;overflow:hidden}
body{position:relative;background:var(--white);font-family:"Open Sans",Arial,sans-serif;color:var(--text)}

/* header */
.site-header{position:absolute;left:0;top:0;width:1200px;height:102px;background:var(--white)}
.brand{position:absolute;left:96px;top:30px;font-family:"Montserrat",sans-serif;font-weight:700;font-size:38px;color:var(--red);letter-spacing:.5px;line-height:1}
.contact-chip{position:absolute;top:35px;display:flex;align-items:center;gap:12px;font-family:"Arimo",Arial,sans-serif;font-size:15px;color:var(--text)}
.contact-chip svg{width:40px;height:40px}
.chip-phone{left:731px}
.chip-mail{left:939px}

.main-nav{position:absolute;left:0;top:102px;width:1200px;height:49px;background:var(--red)}
.main-nav a{position:absolute;top:0;line-height:49px;transform:translateX(-50%);font-family:"Open Sans",sans-serif;font-weight:600;font-size:13.5px;color:var(--white);text-decoration:none;white-space:nowrap}
.main-nav a.active::after{content:"";position:absolute;left:0;right:0;bottom:0;height:3px;background:#9d0c22}

.hero-photo{position:absolute;left:0;top:151px;width:1200px;height:471px;background:linear-gradient(135deg,#8a6a4f 0%,#a47e5c 45%,#6f5846 100%)}

/* intro */
.intro-card{position:absolute;left:81px;top:548px;width:1040px;height:240px;background:var(--white);text-align:center;box-shadow:0 14px 22px -14px rgba(0,0,0,.12)}
.intro-card h1{margin-top:45px;font-family:"Montserrat",sans-serif;font-weight:700;font-size:32px;color:var(--ink)}
.intro-card p{margin:24px auto 0;width:950px;font-size:15px;line-height:23.5px;color:var(--text)}
.intro-notch{position:absolute;left:570px;top:788px;width:0;height:0;border-left:13px solid transparent;border-right:13px solid transparent;border-top:12px solid #eee}

/* services */
.service-card{position:absolute;top:941px;width:239px;height:254px;border:1px solid var(--card-line);background:var(--white);text-align:center}
.service-photo{position:absolute;left:50%;top:-91px;width:168px;height:168px;margin-left:-84px;border-radius:50%;border:3px solid #a8182a;background:var(--white);padding:4px}
.service-photo span{display:block;width:100%;height:100%;border-radius:50%}
.service-card h2{position:absolute;left:0;right:0;top:89px;font-family:"Open Sans",sans-serif;font-weight:700;font-size:15.5px;color:var(--ink);letter-spacing:.3px}
.service-card p{position:absolute;left:12px;right:12px;top:118px;font-family:"Arimo",Arial,sans-serif;font-size:13.5px;line-height:20px;color:var(--text)}
.btn{display:inline-block;background:var(--red-dark);color:var(--white);font-family:"Open Sans",sans-serif;font-weight:600;text-decoration:none}
.service-card .btn{position:absolute;left:50%;transform:translateX(-50%);top:220px;width:100px;height:32px;line-height:32px;font-size:11.5px}

/* book band */
.book-band{position:absolute;left:0;top:1263px;width:1200px;height:437px;background:linear-gradient(90deg,var(--band-b) 0%,var(--band-a) 45%,var(--band-b) 100%);overflow:hidden}
.book-band h2{position:absolute;left:81px;top:83px;font-family:"Montserrat",sans-serif;font-weight:700;font-size:28px;color:var(--ink)}
.book-band p{position:absolute;left:81px;width:400px;font-size:14px;line-height:20px;color:#1c1c1c}
.book-band .btn{position:absolute;left:81px;top:349px;width:149px;height:41px;line-height:41px;padding-left:19px;font-size:12px}
.video-tablet{position:absolute;left:530px;top:103px;width:670px;height:334px;background:linear-gradient(160deg,#e9e9e9 0%,#cfcfcf 30%,#3a3d44 55%,#2a2c31 100%);border-radius:14px 0 0 0}

/* testimonials */
.testimonials{position:absolute;left:0;top:1700px;width:1200px;height:530px;background:var(--pale);text-align:center}
.testimonials h2{margin-top:60px;font-family:"Montserrat",sans-serif;font-weight:600;font-size:30px;color:var(--ink)}
.testimonials blockquote{margin:28px auto 0;width:900px;font-family:"Montserrat",sans-serif;font-size:18.5px;line-height:24px;color:var(--text)}
.avatar{position:absolute;left:536px;top:226px;width:112px;height:112px;border-radius:50%;border:4px solid #dedede;background:linear-gradient(160deg,#cfd8e2,#8a99a8)}
.quote-badge{position:absolute;left:528px;top:228px;width:38px;height:38px;border-radius:50%;background:#2a2a2a;border:3px solid var(--white)}
.quote-badge svg{width:100%;height:100%}
.cite{position:absolute;left:0;right:0;top:378px;font-family:"Open Sans",sans-serif;font-style:italic;font-weight:700;font-size:15px;color:var(--ink)}
.dots{position:absolute;left:536px;top:461px;display:flex;gap:6px}
.dots i{width:30px;height:5px;background:#d6d6d6}
.dots i.on{background:var(--red)}

/* footer */
.site-footer{position:absolute;left:0;top:2230px;width:1200px;height:345px;background:var(--footer);color:var(--footer-text)}
.site-footer h3{position:absolute;top:34px;font-family:"Montserrat",sans-serif;font-weight:400;font-size:25px;color:var(--white)}
.about-text{position:absolute;left:96px;top:82px;width:290px;font-size:14px;line-height:21.5px}
.contact-list{position:absolute;left:487px;top:80px;list-style:none;font-size:12.5px}
.contact-list li{position:relative;display:flex;margin-bottom:14px;line-height:18px}
.contact-list svg{width:16px;height:16px;margin-top:1px;flex:none}
.contact-list b{width:60px;margin-left:18px;font-weight:600;color:#9a9a9a;flex:none}
.contact-list span{color:var(--white);font-weight:600}
.hello-form label{position:absolute;left:804px;font-size:12.5px;font-weight:700;color:var(--white)}
.hello-form label em{color:var(--red);font-style:normal}
.field{position:absolute;left:804px;width:240px;background:var(--white)}
.hello-form .btn{position:absolute;left:953px;top:295px;width:93px;height:32px;line-height:32px;text-align:center;font-size:12.5px;border:0}
.copyright{position:absolute;left:0;top:2575px;width:1200px;height:53px;background:var(--footer-bottom);text-align:center;line-height:53px;font-size:12.5px;color:#8a8a8a}
</style>
</head>
<body>

<header class="site-header">
  <div class="brand">Quorvane</div>
  <div class="contact-chip chip-phone">
    <svg viewBox="0 0 40 40"><circle cx="20" cy="20" r="18" fill="none" stroke="var(--blue-icon)" stroke-width="1.6"/><path d="M14 12c1-1 2-1 3 0l2 3c.5 1 0 2-1 2.5-1 .5 1 4 4 5.5 .8-1 1.6-1.5 2.6-1l3 2c1 1 .8 2-.2 3-3 2.5-8 .2-11.4-3.4S11.5 15 14 12z" fill="none" stroke="var(--blue-icon)" stroke-width="1.5"/></svg>
    <span>+1 555 0142 770</span>
  </div>
  <div class="contact-chip chip-mail">
    <svg viewBox="0 0 40 40"><circle cx="20" cy="20" r="18" fill="none" stroke="var(--blue-icon)" stroke-width="1.6"/><rect x="11.5" y="14" width="17" height="12" fill="none" stroke="var(--blue-icon)" stroke-width="1.5"/><path d="M11.5 14l8.5 7 8.5-7" fill="none" stroke="var(--blue-icon)" stroke-width="1.5"/></svg>
    <span>info@quorvane.net</span>
  </div>
</header>

<nav class="main-nav">
  <a class="active" href="#" style="left:240px">HOME</a>
  <a href="#" style="left:359px">ABOUT US</a>
  <a href="#" style="left:517px">THOUGHT LEADERSHIP</a>
  <a href="#" style="left:689px">SERVICES</a>
  <a href="#" style="left:818px">VIDEOS</a>
  <a href="#" style="left:948px">CONTACT US</a>
</nav>

<div class="hero-photo" role="img" aria-label="Overhead photo of a team working with laptops, tablets and charts around a wooden table"></div>

<section class="intro-card">
  <h1>In Search of Innovation</h1>
  <p>Companies like Orchard, Lumora, Veltrix and noted others have already established their credentials as leaders of innovation. But what about those companies that struggle to innovate yet come up short? They come to Quorvane to help them generate, embed, and sustain innovation as an enabler of growth and a source of competitive advantage.</p>
</section>
<div class="intro-notch"></div>

<article class="service-card" style="left:81px">
  <div class="service-photo"><span role="img" aria-label="Photo of hands reviewing printed bar charts" style="background:linear-gradient(135deg,#f2f2f2,#c9d6ea 60%,#e8b24a)"></span></div>
  <h2>CONSULTING</h2>
  <p>While our work iis firmly grounded in theory and research, we are focused on bringing</p>
  <a class="btn" href="#">VIEW MORE &rarr;</a>
</article>
<article class="service-card" style="left:350px">
  <div class="service-photo"><span role="img" aria-label="Photo of a professional working at a computer in an office" style="background:linear-gradient(135deg,#5b6470,#2f3439 60%,#8d7b6a)"></span></div>
  <h2>EXECUTIVE EDUCATION</h2>
  <p>We consult with both private and public sector organizations. Our goal is to help our clients utilize innovation as a tool to enhance organizational performance.</p>
  <a class="btn" href="#">VIEW MORE &rarr;</a>
</article>
<article class="service-card" style="left:617px">
  <div class="service-photo"><span role="img" aria-label="Photo of a thoughtful man seated with a laptop" style="background:linear-gradient(160deg,#f1f1f1,#9fb6d3 55%,#5c6a7a)"></span></div>
  <h2>BOOKS</h2>
  <p>The Quorvane team are all seasoned executive educaton professionals. We offer a number of executive education programs.</p>
  <a class="btn" href="#">VIEW MORE &rarr;</a>
</article>
<article class="service-card" style="left:881px">
  <div class="service-photo"><span role="img" aria-label="Photo of a man seated with a laptop in a bright room" style="background:linear-gradient(160deg,#f1f1f1,#9fb6d3 55%,#5c6a7a)"></span></div>
  <h2>SPEAKING</h2>
  <p>We stay on top of our field by actively engaging in research, networking with other top people in the field of innovation,</p>
  <a class="btn" href="#">VIEW MORE &rarr;</a>
</article>

<section class="book-band">
  <h2>Order Innovation Kata</h2>
  <p style="top:129px">Innovation Kata reveals 7 secret principles that can help any innovator overcome the roadblocks and blockheads that they will inevitably meet on the path to creativity.</p>
  <p style="top:206px">And these principles do not presuppose an innovation friendly culture. In fact, the profiles in this book will introduce you to innovators who have succeeded even when their organizations' culture was either not particularly friendly to new ideas or even downright hostile.</p>
  <a class="btn" href="#">MORE DETAILS &rarr;</a>
  <div class="video-tablet" role="img" aria-label="Hands holding a tablet playing a video of an innovation workshop"></div>
</section>

<section class="testimonials">
  <h2>Client Testimonials</h2>
  <blockquote>"Lorem ipsum dolor sit amet, consectetur adipiscing elit. Morbi hendrerit elit turpis, a porttitor tellus sollicitudin at. Class aptent taciti sociosqu ad litora torquent per conubia nostra, per inceptos himenaeos."</blockquote>
  <div class="avatar" role="img" aria-label="Client portrait"></div>
  <div class="quote-badge"><svg viewBox="0 0 32 32"><path d="M9 19v-3c0-2 1-3.5 3-4.2l.6 1.2c-1 .5-1.6 1.2-1.6 2h1.8V19zm7 0v-3c0-2 1-3.5 3-4.2l.6 1.2c-1 .5-1.6 1.2-1.6 2h1.8V19z" fill="#fff"/></svg></div>
  <div class="cite">MARISSA COLTON Fitness Enthuisast, TRELLWAY</div>
  <div class="dots"><i class="on"></i><i></i><i></i><i></i></div>
</section>

<footer class="site-footer">
  <h3 style="left:95px">About Quorvane</h3>
  <p class="about-text">Quorvane works with a broad range of national and global clients to utilize "Innovation at Work" to improve business results. We help individuals and organizations through the entire value chain of innovation from idea generation, implementation and value creation.</p>

  <h3 style="left:487px">Contact Us</h3>
  <ul class="contact-list">
    <li><svg viewBox="0 0 16 16"><path d="M8 1a4.5 4.5 0 0 0-4.5 4.5C3.5 9 8 15 8 15s4.5-6 4.5-9.5A4.5 4.5 0 0 0 8 1zm0 6.3a1.8 1.8 0 1 1 0-3.6 1.8 1.8 0 0 1 0 3.6z" fill="#ddd"/></svg><b>Address:</b><span>2140 Harlow Ave<br>Fairmont, CA 90512<br>United States</span></li>
    <li><svg viewBox="0 0 16 16"><path d="M3 2c.6-.6 1.3-.6 1.8 0l1.5 2c.4.6.2 1.2-.4 1.6-.5.3.6 2.4 2.5 3.6.5-.6 1-.8 1.6-.4l2 1.4c.6.5.5 1.2-.1 1.800-2 1.6-5 .2-7-2S1.4 3.8 3 2z" fill="#ddd"/></svg><b>Phone:</b><span>+1 555 0189 334</span></li>
    <li><svg viewBox="0 0 16 16"><rect x="1.5" y="3.5" width="13" height="9" fill="#ddd"/><path d="M1.5 3.5L8 9l6.5-5.5" fill="none" stroke="#2c2c2c" stroke-width="1.2"/></svg><b>E-mail:</b><span>hello@quorvane.net</span></li>
    <li><svg viewBox="0 0 16 16"><circle cx="8" cy="8" r="6.5" fill="#ddd"/></svg><b>Skype:</b><span>quorvane.team</span></li>
  </ul>

  <h3 style="left:804px">Say Hello!</h3>
  <form class="hello-form">
    <label style="top:84px">Name<em>*</em></label>
    <div class="field" style="top:100px;height:28px"></div>
    <label style="top:145px">Email<em>*</em></label>
    <div class="field" style="top:160px;height:30px"></div>
    <label style="top:206px">Message<em>*</em></label>
    <div class="field" style="top:221px;height:60px"></div>
    <span class="btn">SUBMIT</span>
  </form>
</footer>
<div class="copyright">&copy; Copyright 2018 Quorvane. All Right Reserved.</div>

</body>
</html>
```